Commercial Broker Profile Flyer

I need a one-page flyer created that will serve as a profile report for individual brokers within a commercial real estate firm. The flyer will include company branding, agent photo, bio, and other information. I would like to have the source file available for future editing preferably in a Publisher file format. A copy of a company brochure is included and would like to have this profile flyer similar to keep company branding consistent. Our company website is www.holbrookvalere.com for any other questions on branding.
Updates

Target Market(s)

Professional

Industry/Entity Type

Real Estate Agent

Requirements
Must have
• One page
• Source files MUST include a .PUB file that I can update in the future
• All of the information in the uploaded "content" file
• Company branding
• Must be 8.5"x11"
Should not have
• Do not use stock photos or property photos from the attachments. I only want the broker photo and company logo.

```html
<!DOCTYPE html>
<html lang="en">
<head>
<meta charset="utf-8">
<title>Broker Profile – Holbrook Valere Real Estate</title>
<link rel="stylesheet" href="https://fonts.googleapis.com/css2?family=EB+Garamond:wght@700&family=Arimo:wght@400&display=swap">
<style>
  :root {
    --green: #1a6444;
    --green-deep: #14573a;
    --ornament: #cfe3d5;
    --ornament-soft: #eaf3ec;
    --ink: #1b1b1b;
    --backdrop: #7b7b7b;
    --paper: #ffffff;
    --photo-top: #b9bcba;
    --photo-bottom: #6f7370;
  }
  * { margin: 0; padding: 0; box-sizing: border-box; }
  html, body { width: 1200px; height: 1200px; overflow: hidden; }
  body { background: var(--backdrop); font-family: "Arimo", Arial, sans-serif; color: var(--ink); position: relative; }

  .flyer { position: absolute; left: 184px; top: 58px; width: 839px; height: 1085px; background: var(--paper); overflow: hidden; }

  .ornament { position: absolute; }
  .ornament--top { right: 0; top: 0; width: 333px; height: 112px; background: radial-gradient(ellipse at 60% 40%, var(--ornament) 0%, var(--ornament-soft) 60%, rgba(255,255,255,0) 100%); }
  .ornament--bottom { left: 0; top: 920px; width: 333px; height: 117px; background: radial-gradient(ellipse at 40% 60%, var(--ornament) 0%, var(--ornament-soft) 60%, rgba(255,255,255,0) 100%); }

  .brand { position: absolute; left: 52px; top: 100px; font-family: "Arimo", Arial, sans-serif; font-weight: 400; color: var(--green); font-size: 34px; line-height: 1; }

  .rule { position: absolute; left: 48px; width: 740px; height: 3px; background: var(--green-deep); }
  .rule--top { top: 199px; }
  .rule--bottom { top: 557px; }

  .portrait { position: absolute; left: 49px; top: 222px; width: 226px; height: 317px; background: linear-gradient(160deg, var(--photo-top), var(--photo-bottom)); }

  .profile { position: absolute; left: 301px; top: 225px; width: 488px; }
  .profile__name { font-family: "EB Garamond", Georgia, serif; font-weight: 700; color: var(--green); font-size: 19px; letter-spacing: 0.5px; }
  .profile__name small { font-size: 14px; }
  .profile__title { font-size: 16.5px; margin-top: 1px; }
  .contact { list-style: none; margin-top: 2px; }
  .contact li { display: flex; align-items: center; gap: 9px; font-size: 16px; height: 23px; }
  .contact svg { width: 18px; height: 18px; fill: var(--green); flex: none; }
  .bio { font-size: 11.6px; line-height: 14.5px; margin-top: 14px; letter-spacing: -0.1px; }
  .bio + .bio { margin-top: 6px; }

  .section { position: absolute; left: 301px; }
  .section__title { font-family: "EB Garamond", Georgia, serif; font-weight: 700; color: var(--green); font-size: 19px; }
  .section--clients { top: 594px; }
  .section--affiliations { top: 866px; }
  .clients { list-style: none; margin-top: 6px; }
  .clients li { display: flex; align-items: center; gap: 8px; font-size: 16.5px; height: 22.5px; }
  .clients svg { width: 16px; height: 16px; flex: none; }
  .affiliations { list-style: none; margin-top: 8px; }
  .affiliations li { font-size: 16.5px; line-height: 19.8px; }

  .footer-band { position: absolute; left: 0; bottom: 0; width: 100%; height: 48px; background: var(--green-deep); }
</style>
</head>
<body>
<main class="flyer">
  <div class="ornament ornament--top" role="img" aria-label="Decorative pale green scroll ornament"></div>
  <div class="ornament ornament--bottom" role="img" aria-label="Decorative pale green scroll ornament"></div>

  <header class="brand">Holbrook Valere Real Estate</header>

  <div class="rule rule--top"></div>

  <div class="portrait" role="img" aria-label="Broker portrait photo"></div>

  <section class="profile">
    <h1 class="profile__name">T. DECLAN HOLBROOK, <small>CCAM, CRLP</small></h1>
    <p class="profile__title">Principal / Broker in Charge</p>
    <ul class="contact">
      <li><svg viewBox="0 0 24 24"><path d="M3 9c0-3 4-5 9-5s9 2 9 5v2h-5V9H8v2H3zM6 12h12l2 8H4z"/></svg>(555) 214-3080 ext. 202</li>
      <li><svg viewBox="0 0 24 24"><path d="M7 2h10a2 2 0 0 1 2 2v16a2 2 0 0 1-2 2H7a2 2 0 0 1-2-2V4a2 2 0 0 1 2-2zm0 3v13h10V5z"/></svg>(555) 367-9142</li>
      <li><svg viewBox="0 0 24 24"><path d="M2 5h20v14H2zm2 2v1l8 5 8-5V7l-8 5z"/></svg>declan@holbrookvalere.com</li>
      <li><svg viewBox="0 0 24 24"><path d="M12 2a10 10 0 1 0 0 20 10 10 0 0 0 0-20zm0 2c1.5 1.6 2.4 4 2.6 7H9.4c.2-3 1.1-5.4 2.6-7zM4.1 11a8 8 0 0 1 5-6.3C8 6.6 7.5 8.7 7.4 11zm0 2h3.3c.1 2.3.6 4.4 1.7 6.3a8 8 0 0 1-5-6.3zm5.3 0h5.2c-.2 3-1.1 5.4-2.6 7-1.5-1.6-2.4-4-2.6-7zm7.2 0h3.3a8 8 0 0 1-5 6.3c1.1-1.9 1.6-4 1.7-6.3zm0-2c-.1-2.3-.6-4.4-1.7-6.3a8 8 0 0 1 5 6.3z"/></svg>www.holbrookvalere.com</li>
    </ul>
    <p class="bio">Declan began his real estate career in 2005 and has completed $75+ million in transactions representing sellers and buyers of commercial real estate, providing tenant representation, and leasing of retail and office properties. Prior to beginning his real estate career, Declan served over five years in the National Guard and attended Eastern State University.</p>
    <p class="bio">Declan has earned the respected Certified Commercial Asset Member (CCAM) designation as well as the Certified Retail Leasing Professional (CRLP) designation. Declan is a member of the Global Council of Retail Properties (GCRP), the State and Ridgeport Realtor Associations, the Ridgeport County Chamber of Commerce, and serves on the board of directors for the state CCAM Chapter, the Sandhill Community Center, and the Tall Cedar Realtors Association. Declan is a licensed broker in two states.</p>
  </section>

  <div class="rule rule--bottom"></div>

  <section class="section section--clients">
    <h2 class="section__title">Clients Served</h2>
    <ul class="clients">
      <li><svg viewBox="0 0 16 16"><circle cx="8" cy="8" r="8" fill="#1a6444"/><path d="M4.3 8.2l2.5 2.4 4.9-5" stroke="#fff" stroke-width="2" fill="none"/></svg>Hearthside Chicken</li>
      <li><svg viewBox="0 0 16 16"><circle cx="8" cy="8" r="8" fill="#1a6444"/><path d="M4.3 8.2l2.5 2.4 4.9-5" stroke="#fff" stroke-width="2" fill="none"/></svg>Copper Kettle Burgers</li>
      <li><svg viewBox="0 0 16 16"><circle cx="8" cy="8" r="8" fill="#1a6444"/><path d="M4.3 8.2l2.5 2.4 4.9-5" stroke="#fff" stroke-width="2" fill="none"/></svg>Fairway Cuts</li>
      <li><svg viewBox="0 0 16 16"><circle cx="8" cy="8" r="8" fill="#1a6444"/><path d="M4.3 8.2l2.5 2.4 4.9-5" stroke="#fff" stroke-width="2" fill="none"/></svg>Tread Depot</li>
      <li><svg viewBox="0 0 16 16"><circle cx="8" cy="8" r="8" fill="#1a6444"/><path d="M4.3 8.2l2.5 2.4 4.9-5" stroke="#fff" stroke-width="2" fill="none"/></svg>Sugarleaf Bakery</li>
      <li><svg viewBox="0 0 16 16"><circle cx="8" cy="8" r="8" fill="#1a6444"/><path d="M4.3 8.2l2.5 2.4 4.9-5" stroke="#fff" stroke-width="2" fill="none"/></svg>Brightwell Home Care</li>
      <li><svg viewBox="0 0 16 16"><circle cx="8" cy="8" r="8" fill="#1a6444"/><path d="M4.3 8.2l2.5 2.4 4.9-5" stroke="#fff" stroke-width="2" fill="none"/></svg>Kinbridge Services</li>
      <li><svg viewBox="0 0 16 16"><circle cx="8" cy="8" r="8" fill="#1a6444"/><path d="M4.3 8.2l2.5 2.4 4.9-5" stroke="#fff" stroke-width="2" fill="none"/></svg>Townline Media</li>
      <li><svg viewBox="0 0 16 16"><circle cx="8" cy="8" r="8" fill="#1a6444"/><path d="M4.3 8.2l2.5 2.4 4.9-5" stroke="#fff" stroke-width="2" fill="none"/></svg>Clearbrook Beverage Co.</li>
    </ul>
  </section>

  <section class="section section--affiliations">
    <h2 class="section__title">Professional Affiliations</h2>
    <ul class="affiliations">
      <li>Certified Commercial Asset Member (designee)</li>
      <li>Global Council of Retail Properties</li>
      <li>Tall Cedar Realtors Association</li>
      <li>State Realtors Commercial Forms Committee</li>
    </ul>
  </section>

  <div class="footer-band"></div>
</main>
</body>
</html>
```